Business Card Design For Marketing Agnecy LVT

Need business card design for marketing agency.

Dorian Pell
President, CEO
1-555-304-2917
dorian@lumenvaletrewards.net
www.LumenValeTrewards.biz

Back Side:
Boost Sales Using Rewards, Incentives & Giveaways
Get A Free Sample Package

Target Market(s)

B2B

Industry/Entity Type

Marketing

Contact Information for Business Card

Dorian Pell
President, CEO
1-555-304-2917

Back Side:
Get A Free Sample Package

Please note that my current url is OLD DESIGN. I am working on new design and want the business card to match color themes at least on new site. Here is the demo link for new site so you can see the colors I use, etc.

http://pagekilnstudio.example/qx/dorian/lvt_final/index.html

Requirements
Must have
• Please note that my current url is OLD DESIGN. I am working on new design and want the business card to match color themes at least on new site. Here is the demo link for new site so you can see the colors I use, etc.

Nice to have

Should not have

```html
<!DOCTYPE html>
<html lang="en">
<head>
<meta charset="utf-8">
<title>LVT Business Card</title>
<link rel="stylesheet" href="https://fonts.googleapis.com/css2?family=Bebas+Neue&family=Josefin+Sans:wght@300;400;600&family=Montserrat:wght@700&display=swap">
<style>
  :root {
    --page: #ececec;
    --paper: #f4f4f4;
    --blue: #1b6bb0;
    --green: #43a047;
    --charcoal: #4a4a4c;
    --white: #ffffff;
  }
  * { margin: 0; padding: 0; box-sizing: border-box; }
  html, body { width: 1200px; height: 1200px; overflow: hidden; background: var(--page); }
  .canvas { position: relative; width: 1200px; height: 1200px; }
  .card {
    position: absolute; left: 227px; width: 746px; height: 426px;
    border-radius: 28px; overflow: hidden; background: var(--paper);
  }
  .card--front { top: 135px; }
  .card--back { top: 638px; }
  .card-art { position: absolute; inset: 0; width: 100%; height: 100%; }

  /* Front */
  .brand-block { position: absolute; left: 27px; top: 40px; display: flex; align-items: flex-start; gap: 12px; }
  .brand-dot { width: 22px; height: 22px; border-radius: 50%; background: var(--blue); margin-top: 8px; flex: none; }
  .brand-name {
    font-family: "Montserrat", sans-serif; font-weight: 700; color: var(--blue);
    font-size: 40px; line-height: 1.08; letter-spacing: 0.5px; text-transform: uppercase;
  }
  .holder { position: absolute; left: 28px; top: 338px; font-family: "Josefin Sans", sans-serif; color: var(--white); }
  .holder-name { font-size: 26px; font-weight: 600; letter-spacing: 0.3px; }
  .holder-title { font-size: 19px; font-weight: 300; margin-top: 6px; letter-spacing: 0.3px; }
  .contact-list {
    position: absolute; right: 26px; top: 318px; list-style: none;
    font-family: "Josefin Sans", sans-serif; font-weight: 300; font-size: 17px; color: var(--white);
  }
  .contact-item { display: flex; justify-content: flex-end; align-items: center; height: 27.5px; gap: 16px; letter-spacing: 0.3px; }
  .contact-icon { width: 19px; height: 19px; flex: none; }

  /* Back */
  .back-brand {
    position: absolute; top: 62px; left: 0; right: 0; display: flex; justify-content: center; align-items: center; gap: 14px;
  }
  .back-brand .brand-dot { margin-top: 0; width: 20px; height: 20px; }
  .back-brand .brand-name { font-size: 34px; line-height: 1; }
  .tagline {
    position: absolute; top: 150px; left: 0; right: 0; text-align: center;
    font-family: "Bebas Neue", sans-serif; font-size: 31px; color: var(--charcoal); letter-spacing: 0.2px;
  }
  .tagline-boost { color: var(--green); font-size: 35px; }
  .tagline-giveaways { color: var(--blue); font-size: 35px; }
  .offer {
    position: absolute; top: 245px; left: 0; right: 0; text-align: center;
    font-family: "Bebas Neue", sans-serif; font-size: 33px; line-height: 40px; color: var(--white); letter-spacing: 0.3px;
  }
  .back-url {
    position: absolute; top: 358px; left: 0; right: 0; text-align: center;
    font-family: "Bebas Neue", sans-serif; font-size: 27px; color: var(--white); letter-spacing: 0.2px;
  }
</style>
</head>
<body>
<main class="canvas">

  <section class="card card--front">
    <svg class="card-art" viewBox="0 0 746 426" preserveAspectRatio="none" aria-hidden="true">
      <path fill="none" stroke="var(--green)" stroke-width="4" d="M0,278 C260,300 520,240 746,150"/>
      <path fill="var(--blue)" d="M0,292 C260,314 520,254 746,164 L746,426 L0,426 Z"/>
    </svg>

    <div class="brand-block">
      <span class="brand-dot"></span>
      <p class="brand-name">Lumen<br>Vale<br>Trewards</p>
    </div>

    <div class="holder">
      <p class="holder-name">Dorian Pell</p>
      <p class="holder-title">President, CEO</p>
    </div>

    <ul class="contact-list">
      <li class="contact-item">1-555-304-2917
        <svg class="contact-icon" viewBox="0 0 20 20" aria-label="Phone"><circle cx="10" cy="10" r="10" fill="var(--white)"/><path d="M5,9 Q10,4 15,9 L13.5,10.5 L12,9 L8,9 L6.5,10.5 Z M7,11 L13,11 L14,15 L6,15 Z" fill="var(--blue)"/></svg>
      </li>
      <li class="contact-item">dorian@lumenvaletrewards.net
        <svg class="contact-icon" viewBox="0 0 20 20" aria-label="Email"><circle cx="10" cy="10" r="10" fill="var(--white)"/><rect x="5" y="6.5" width="10" height="7" fill="none" stroke="var(--blue)" stroke-width="1.3"/><path d="M5,6.5 L10,11 L15,6.5" fill="none" stroke="var(--blue)" stroke-width="1.3"/></svg>
      </li>
      <li class="contact-item">www.LumenValeTrewards.biz
        <svg class="contact-icon" viewBox="0 0 20 20" aria-label="Website"><circle cx="10" cy="10" r="10" fill="var(--white)"/><circle cx="10" cy="10" r="5.5" fill="none" stroke="var(--blue)" stroke-width="1.3"/><path d="M4.5,10 H15.5 M10,4.5 C7,7 7,13 10,15.5 C13,13 13,7 10,4.5" fill="none" stroke="var(--blue)" stroke-width="1.1"/></svg>
      </li>
    </ul>
  </section>

  <section class="card card--back">
    <svg class="card-art" viewBox="0 0 746 426" aria-hidden="true">
      <rect x="0" y="229" width="746" height="76" fill="var(--green)"/>
      <rect x="0" y="305" width="746" height="121" fill="var(--blue)"/>
    </svg>

    <div class="back-brand">
      <span class="brand-dot"></span>
      <p class="brand-name">Lumen Vale Trewards</p>
    </div>

    <p class="tagline"><span class="tagline-boost">Boost</span> Sales Using Rewards, Incentives &amp; <span class="tagline-giveaways">Giveaways</span></p>
    <p class="offer">Get A Free Sample Package</p>
    <p class="back-url">www.LumenValeTrewards.biz</p>
  </section>

</main>
</body>
</html>
```